Email Marketing for HR and Career Consulting Company

I am looking for a email marketing template that will be developed in HTML format. Right now, we need PSD file format.

The content will include:

1. Featured / Poplar Blog post
2. Latest blog post this week
3. Latest jobs this week
4. Connect with us (social media)

This is a bi-weekly template which we will be sending to people who sign up our weekly newsletter. The purpose of the newsletter is to provide career advise and also latest jobs that's available from our company so that we can redirect them to our career page or apply to our latest jobs.
Updates

Project Deadline Extended
Reason: I am extending this deadline as I would like to see more designs. So far, I have only shortlisted one design that is close to what I am looking for. To all designers, please note that your design would have to be practical and easy to navigate. It also must take into consideration that when we develop this into html, it will b responsive.

Target Market(s)

Job seekers - age group 25 - 45

Industry/Entity Type

Consulting

Font styles to use
Other font styles liked:
• Helvetical

Colors
0492cd
e34197
ec1f27
85cae6
33a6d7
85acd3
eda3c7
e667a6
f59195

Requirements
Must have
• 1. Social media icons
• 2. Links - jobs, contact us
• 3. Popular career advice
• 4. Latest career advice
• 5. Featured jobs
• 6. Popular jobs
Nice to have
• I would like to see clean and minimalist design. Please try to avoid black color. Use pastel colors as much as possible. Our website is www.careerpondly.com.sg
Should not have
• Should avoid black and dark colors

```html
<!DOCTYPE html>
<html lang="en">
<head>
<meta charset="utf-8">
<title>CareerPond Newsletter</title>
<link href="https://fonts.googleapis.com/css2?family=Roboto:ital,wght@0,400;0,500;0,700;1,400&display=swap" rel="stylesheet">
<style>
:root{
  --blue:#0492cd;
  --blue-bright:#1fa3dc;
  --blue-soft:#85cae6;
  --page:#eeeeee;
  --white:#ffffff;
  --text:#555555;
  --muted:#888888;
  --rule:#e2e2e2;
  --footer:#222222;
  --footer-deep:#161616;
  --footer-text:#cfcfcf;
}
*{box-sizing:border-box;margin:0;padding:0}
html,body{width:1200px;height:2568px;overflow:hidden}
body{background:var(--page);font-family:"Roboto",Arial,sans-serif;color:var(--text);position:relative}
.pre-header{position:absolute;top:20px;left:0;width:1200px;text-align:center;font-size:14px;color:#444}
.pre-header a{color:#e34197;text-decoration:underline}
.mail{position:absolute;left:180px;top:160px;width:840px;height:2246px;background:var(--white)}
.top-bar{position:absolute;left:0;top:0;width:840px;height:40px;background:var(--blue-bright);display:flex;align-items:center;padding:0 20px;color:var(--white);font-size:14px}
.top-bar .item{display:flex;align-items:center;gap:8px;margin-right:26px}
.top-bar .socials{margin-left:auto;display:flex;gap:8px}
.dot{width:22px;height:22px;border-radius:50%;border:2px solid var(--white)}
.brand{position:absolute;top:62px;left:0;width:840px;text-align:center}
.brand-mark{width:74px;height:74px;border-radius:50%;background:var(--blue-bright);margin:0 auto}
.brand-name{margin-top:6px;font-size:18px;font-weight:500;color:var(--blue-bright)}
.hero{position:absolute;top:208px;left:48px;width:744px;height:312px}
.hero .main{position:absolute;left:0;top:0;width:472px;height:312px;background:linear-gradient(135deg,#6c6a63,#3c3f43 60%,#8a7a62)}
.hero .side-a{position:absolute;left:492px;top:0;width:252px;height:144px;background:linear-gradient(135deg,#b9b4a6,#8b8777)}
.hero .side-b{position:absolute;left:492px;top:160px;width:252px;height:152px;background:linear-gradient(135deg,#d8d2c4,#c7312c 70%)}
.section-title{position:absolute;display:flex;align-items:center;gap:10px;font-size:20px;font-weight:700;color:#444}
.about{position:absolute;left:48px;top:620px;width:744px;font-size:16px;line-height:27px;color:var(--muted)}
.about p+p{margin-top:24px}
.btn-outline{position:absolute;left:355px;top:800px;width:130px;height:36px;border:1px solid var(--blue-bright);border-radius:3px;color:var(--blue-bright);font-size:13px;display:flex;align-items:center;justify-content:center}
.card{position:absolute;top:970px;width:344px;height:340px;background:var(--white)}
.card .art{height:220px}
.card .meta{display:flex;height:120px}
.card .date{width:118px;background:var(--blue-bright);color:var(--white);font-size:19px;font-weight:700;padding:20px 12px;line-height:26px}
.card .info{flex:1;padding:18px 14px;font-size:13px;line-height:19px;color:#444}
.card .info .by{color:var(--blue-bright);font-style:italic}
.btn-fill{position:absolute;left:350px;top:1364px;width:140px;height:40px;background:var(--blue-bright);border-radius:3px;color:var(--white);font-size:13px;font-weight:500;display:flex;align-items:center;justify-content:center}
.cats{position:absolute;left:48px;top:1552px;width:460px;display:grid;grid-template-columns:1fr 1fr;row-gap:20px;column-gap:20px;font-size:14px;color:var(--muted)}
.cats li{list-style:none;display:flex;align-items:center;gap:10px}
.cats li::before{content:"";width:14px;height:14px;border:1.5px solid #999;border-radius:50%}
.jobs{position:absolute;left:540px;top:1552px;width:252px}
.job{margin-bottom:26px}
.job h4{font-size:14px;font-weight:700;color:var(--blue-bright);line-height:20px}
.job p{font-size:13px;font-style:italic;color:var(--muted);line-height:19px;margin-top:6px}
.jobs .more{font-size:14px;font-style:italic;color:var(--blue-bright)}
.divider{position:absolute;left:520px;top:1500px;width:1px;height:380px;background:var(--rule)}
.footer{position:absolute;left:0;top:1950px;width:840px;height:240px;background:var(--footer)}
.footer .links{position:absolute;left:48px;top:58px;width:130px}
.footer .links span{display:block;font-size:13px;color:var(--footer-text);padding:10px 8px;border-bottom:1px solid #3a3a3a}
.footer .f-brand{position:absolute;left:0;width:840px;top:48px;text-align:center}
.footer .f-brand .brand-mark{width:80px;height:80px;background:#555}
.footer .f-brand .brand-name{color:#bbb}
.footer .contact{position:absolute;left:600px;top:62px;font-size:13px;color:var(--footer-text)}
.footer .contact div{display:flex;align-items:center;gap:10px;margin-bottom:18px}
.footer .contact .socials{display:flex;gap:8px}
.footer .dot{border-color:var(--footer-text)}
.copyright{position:absolute;left:0;top:2190px;width:840px;height:50px;background:var(--footer-deep);color:#aaa;font-size:13px;display:flex;align-items:center;justify-content:center}
.base-line{position:absolute;left:0;top:2240px;width:840px;height:6px;background:var(--blue-bright)}
</style>
</head>
<body>
<div class="pre-header">For anything about this mail you can contact us by <a>click this link</a></div>

<main class="mail">
  <header class="top-bar">
    <div class="item">
      <svg width="16" height="16" viewBox="0 0 24 24"><path fill="#fff" d="M6.6 10.8a15 15 0 0 0 6.6 6.6l2.2-2.2c.3-.3.7-.4 1-.2 1.1.4 2.3.6 3.6.6.6 0 1 .4 1 1V20c0 .6-.4 1-1 1A17 17 0 0 1 3 4c0-.6.4-1 1-1h3.5c.6 0 1 .4 1 1 0 1.3.2 2.5.6 3.6.1.3 0 .7-.2 1z"/></svg>
      0800 555 210
    </div>
    <div class="item">
      <svg width="18" height="14" viewBox="0 0 18 14"><rect x="1" y="1" width="16" height="12" fill="none" stroke="#fff" stroke-width="1.6"/><path d="M1 1l8 7 8-7" fill="none" stroke="#fff" stroke-width="1.6"/></svg>
      hello@careerpondly.com.sg
    </div>
    <div class="socials"><span class="dot"></span><span class="dot"></span><span class="dot"></span></div>
  </header>

  <div class="brand">
    <div class="brand-mark"></div>
    <div class="brand-name">careerpond</div>
  </div>

  <div class="hero">
    <div class="main" role="img" aria-label="Photo of a desk workspace with the word jobs"></div>
    <div class="side-a" role="img" aria-label="Photo of a maze with job lettering"></div>
    <div class="side-b" role="img" aria-label="Photo of a new job sign"></div>
  </div>

  <div class="section-title" style="left:48px;top:574px">
    <svg width="14" height="22" viewBox="0 0 14 22"><rect x="0" y="0" width="4" height="22" fill="#1fa3dc"/><rect x="7" y="0" width="7" height="4" fill="#1fa3dc"/></svg>
    What We Do:
  </div>
  <div class="about">
    <p>Since CareerPond first started office in 2011, it is widely known as a logistics recruitment specialist who understands the dynamics and role requirements of this arena.</p>
    <p>With our credentials, partnerships and recruiting alliances in Singapore, Malaysia and China, our award winning team have since widened our network to cover supply chain and energy sectors clients.</p>
  </div>
  <div class="btn-outline">READ MORE »</div>

  <div class="section-title" style="left:48px;top:914px">
    <svg width="14" height="22" viewBox="0 0 14 22"><rect x="0" y="0" width="4" height="22" fill="#1fa3dc"/><rect x="7" y="0" width="7" height="4" fill="#1fa3dc"/></svg>
    Featured / Poplar Blog post :
  </div>

  <article class="card" style="left:48px">
    <div class="art" role="img" aria-label="Illustration of an office worker waving goodbye" style="background:linear-gradient(135deg,#85cae6,#6fb8d9)"></div>
    <div class="meta">
      <div class="date">July 26,<br>2016</div>
      <div class="info">10 Things to Expect After You Have Quit Your Job<br><span class="by">by Lena Ong</span></div>
    </div>
  </article>
  <article class="card" style="left:448px">
    <div class="art" role="img" aria-label="Illustration of a hand reaching for a ringing telephone" style="background:linear-gradient(135deg,#e8735a,#d9523c 55%,#33a6d7)"></div>
    <div class="meta">
      <div class="date">July 26,<br>2016</div>
      <div class="info">5 Reasons You're Not Getting Phone Calls During Your Job Search <span class="by">by Lena Ong</span></div>
    </div>
  </article>

  <div class="btn-fill">READ MORE »</div>

  <div class="divider"></div>
  <div class="section-title" style="left:48px;top:1498px">
    <svg width="14" height="22" viewBox="0 0 14 22"><rect x="0" y="0" width="4" height="22" fill="#1fa3dc"/><rect x="7" y="0" width="7" height="4" fill="#1fa3dc"/></svg>
    Watch our job Categoris :
  </div>
  <div class="section-title" style="left:540px;top:1498px">
    <svg width="14" height="22" viewBox="0 0 14 22"><rect x="0" y="0" width="4" height="22" fill="#1fa3dc"/><rect x="7" y="0" width="7" height="4" fill="#1fa3dc"/></svg>
    Latest jobs this week :
  </div>

  <ul class="cats">
    <li>Advertising &amp; Sponsorship (29)</li><li>Digital (28)</li>
    <li>Account Management (10)</li><li>Insight (138)</li>
    <li>Brand &amp; Product (84)</li><li>PR &amp; Media (118)</li>
    <li>Business Development (8)</li><li>Sales (35)</li>
    <li>Campaign Management (142)</li><li>Creative (56)</li>
    <li>Category Management (12)</li><li>Trade (50)</li>
    <li>Communications (188)</li><li>Other (20)</li>
  </ul>

  <div class="jobs">
    <div class="job">
      <h4>INTERNATIONAL MARKETING MANAGER LIGHTWATER -</h4>
      <p>Between £40,000 and £50,000 per job package</p>
    </div>
    <div class="job">
      <h4>INTERIM HEAD OF ALUMNI AND SUPPORTER ENGAGEMENT</h4>
      <p>Between £40,000 and £50,000 per job package</p>
    </div>
    <div class="more">Read More»</div>
  </div>

  <footer class="footer">
    <div class="links"><span>View in browser</span><span>Unsubscribe</span><span>Send to a friend</span></div>
    <div class="f-brand">
      <div class="brand-mark"></div>
      <div class="brand-name">careerpond</div>
    </div>
    <div class="contact">
      <div>
        <svg width="16" height="16" viewBox="0 0 24 24"><path fill="#cfcfcf" d="M6.6 10.8a15 15 0 0 0 6.6 6.6l2.2-2.2c.3-.3.7-.4 1-.2 1.1.4 2.3.6 3.6.6.6 0 1 .4 1 1V20c0 .6-.4 1-1 1A17 17 0 0 1 3 4c0-.6.4-1 1-1h3.5c.6 0 1 .4 1 1 0 1.3.2 2.5.6 3.6.1.3 0 .7-.2 1z"/></svg>
        Singapore 018956
      </div>
      <div>
        <svg width="18" height="14" viewBox="0 0 18 14"><rect x="1" y="1" width="16" height="12" fill="none" stroke="#cfcfcf" stroke-width="1.6"/><path d="M1 1l8 7 8-7" fill="none" stroke="#cfcfcf" stroke-width="1.6"/></svg>
        hello@careerpondly.com.sg
      </div>
      <div class="socials"><span class="dot"></span><span class="dot"></span><span class="dot"></span><span class="dot"></span></div>
    </div>
  </footer>
  <div class="copyright">©2016 All Right Reserved. CareerPond Pte Limited.</div>
  <div class="base-line"></div>
</main>
</body>
</html>
```